Shaping Lattice Engineering

We need to design the look and feel for an innovation company with software products for solving complex IT problems following socio-technical theory thinking. The company is heavy in designing of complex systems (like an architect shop). The new design will form the foundation of our brand moving forward. We will approach software projects as if one is building a skyscraper or a bridge. We want to humanize technology and not the other way around. Our target groups will be healthcare and the environment. We will be able to take complex problems and turn them into amazing IT solutions that improve the quality of life for people.

Here are more fragments of ideas that can help:
===============

Motivation

The technology described in the application, coincides with “Steer-Via-Pulse” concept of Lorne Vistrup, which suggests managing a business by managing an informational representation of it : Lorne had the following vision:

"Imagine an enterprise design model that defines the behavior of an entire business. Imagine making this model a part of the corporate informational infrastructure, implementing it on technology that connects all relevant sources and users of information and affords maximum sharing among all parts of the firm. Managers could respond to the read-outs appearing on the console, modifying the flight plan en route based on changes in external conditions, monitoring the performance of delegated responsibilities, sending coordinated directions to subsidiary functions, and experiencing exhilaration upon their execution. It constitutes institutional memory and intelligence, which augment management's ability to run the business”.

This product does what Mr. Vistrup envisioned.

The Objective

QTV offers software products for the specification, construction, assembly, and ongoing management of a digital representation that is an exact mirror image of an enterprise. The main idea is the capability of managing the enterprise by managing an information technology representation of it through software. The idea is to manage the enterprise as a total system involving all aspects of operations. That makes the enterprise and all its information technology representation is inseparable. The implication is that the management of change at the business and IT infrastructure levels are unified. For example, by reconfiguring the information representation of the enterprise one can change business performance. By changing the configuration of the business representation one can actually change the organization’s ability to respond to internal and external events. Management leadership can act with the aid of technology to better respond and improve their ability to guide the organization. The knowledge management feature of the digital representation of the enterprise enables managers to monitor the impact of change and therefore help management assess risk and determine whether mitigating responses are necessary.

The technology and product defines a new approach for the design, implementation, and ongoing execution of software systems that are truly business-like rather than applications and workflows.

Software

```html
<!DOCTYPE html>
<html lang="en">
<head>
<meta charset="utf-8">
<title>Shaping Lattice Engineering</title>
<link href="https://fonts.googleapis.com/css2?family=Open+Sans:wght@300;400&family=PT+Sans+Narrow:wght@400;700&display=swap" rel="stylesheet">
<style>
:root{
  --teal:#1e9ab8;
  --band:#3f8ea6;
  --ink:#222;
  --muted:#333;
  --rule:#bbb;
  --link-red:#a4262c;
  --footer:#1f1f1f;
  --footer-text:#ddd;
}
*{margin:0;padding:0;box-sizing:border-box}
html,body{width:1200px;height:1200px;overflow:hidden}
body{position:relative;background:var(--footer);font-family:Arial,Helvetica,sans-serif;color:var(--ink)}
.abs{position:absolute}

/* header */
.site-header{left:0;top:0;width:1200px;height:86px;background:linear-gradient(#3a3a3a,#0a0a0a 70%,#000)}
.brand-name{left:118px;top:26px;font-family:'Open Sans',sans-serif;font-weight:400;font-size:26px;color:#f2f2f2}
.utility-links{left:902px;top:51px;font-size:11px;color:var(--teal)}
.utility-links span{margin:0 6px;color:#4aa8c0}

/* nav */
.main-nav{left:0;top:86px;width:1200px;height:47px;background:linear-gradient(#fff,#e6e6e6);border-bottom:6px solid #1a1a1a}
.main-nav ul{list-style:none;position:absolute;left:110px;top:0;display:flex}
.main-nav li{height:41px;line-height:39px;text-align:center;font-family:'PT Sans Narrow',sans-serif;font-size:15px;color:#222;border-right:1px solid #cfcfcf}
.main-nav li.active{background:linear-gradient(#2b8aa3,#166a80);color:#fff}

/* hero */
.hero{left:0;top:133px;width:1200px;height:436px;background:linear-gradient(90deg,#9fc4d8 0%,#5d8aa3 18%,#2d5a72 40%,#1f4a5e 60%,#3c5b68 80%,#1b2126 100%)}
.hero-list{left:500px;top:67px;width:225px}
.hero-item{position:absolute;left:0;width:220px;height:60px;border-bottom:1px solid rgba(255,255,255,.55);text-align:right;padding-right:43px}
.hero-item h3{font-weight:400;font-size:16px;color:#fff;margin-top:13px}
.hero-item p{font-size:12px;color:#d5e8f0}
.hero-item svg{position:absolute;right:0;top:12px}
.hero-arrow{top:186px}

/* band */
.promo-band{left:0;top:570px;width:1200px;height:50px;background:var(--band);border-top:2px solid #2d7288}
.promo-band h2{position:absolute;left:318px;top:8px;font-family:'Open Sans',sans-serif;font-weight:300;font-size:23px;color:#fff}
.inquire-btn{position:absolute;left:912px;top:6px;width:159px;height:34px;border-radius:5px;background:linear-gradient(#fff,#dfe8ec);font-weight:700;font-size:14px;color:#223;line-height:34px;padding-left:23px}
.inquire-btn svg{position:absolute;right:12px;top:12px}

/* content */
.content{left:0;top:620px;width:1200px;height:394px;background:#fff}
.col-rule{top:40px;width:1px;height:311px;background:var(--rule)}
.col-title{font-family:'Open Sans',sans-serif;font-weight:300;font-size:27px;color:#222}
.service{width:260px}
.service .icon{position:absolute;left:0;top:0;width:50px;height:40px;border-radius:6px}
.service h4{position:absolute;left:57px;top:0;font-size:14px;color:var(--teal);font-weight:700}
.service p{position:absolute;left:57px;top:19px;font-size:12px;line-height:14px;color:var(--muted);width:200px}
.why h4{font-family:'Open Sans',sans-serif;font-weight:300;font-size:22px;line-height:26px;color:var(--teal)}
.why p{font-size:12px;line-height:14px;color:var(--muted);width:280px}
.why a,.about a{color:var(--link-red)}
.why a{font-size:11px;text-decoration:underline}
.about p{font-size:12px;line-height:14.5px;color:var(--muted);width:270px;margin-bottom:14px}
.about a{font-family:'Open Sans',sans-serif;font-size:16px;text-decoration:none}

/* footer */
.footer-brand{left:136px;top:1045px;font-family:'Open Sans',sans-serif;font-size:19px;color:#fff}
.copyright{left:140px;top:1079px;font-size:11px;color:var(--footer-text)}
.footer-col h5{font-family:'PT Sans Narrow',sans-serif;font-weight:700;font-size:19px;color:#fff;margin-bottom:12px}
.footer-col ul{list-style:none}
.footer-col li{font-size:12px;color:var(--teal);height:22px;padding-left:12px;position:relative;letter-spacing:.2px}
.footer-col li::before{content:"";position:absolute;left:0;top:4px;border-left:4px solid #ccc;border-top:3px solid transparent;border-bottom:3px solid transparent}
.email-field{left:859px;top:1075px;width:185px;height:26px;border-radius:3px;background:#141414;border:1px solid #444;font-size:12px;color:#999;padding:6px 15px}
.subscribe-btn{left:968px;top:1113px;width:81px;height:27px;border-radius:4px;background:linear-gradient(#2aa3c2,#17809c);color:#fff;font-family:'PT Sans Narrow',sans-serif;font-size:13px;text-align:center;line-height:27px}
</style>
</head>
<body>

<header class="site-header abs">
  <div class="brand-name abs">Shaping Lattice Engineering</div>
  <div class="utility-links abs">Support<span>|</span>FAQs<span>|</span>Site Map<span>|</span>Help</div>
</header>

<nav class="main-nav abs">
  <ul>
    <li class="active" style="width:134px">Home</li>
    <li style="width:140px">About Us</li>
    <li style="width:140px">Products</li>
    <li style="width:140px">Solutions</li>
    <li style="width:140px">Downloads</li>
    <li style="width:141px">Support</li>
    <li style="width:140px;border-right:0">Contacts</li>
  </ul>
</nav>

<section class="hero abs" role="img" aria-label="Photo of a glass skyscraper on the left and a businessman holding a laptop on the right, with blue digital circuit graphics">
  <svg class="abs hero-arrow" style="left:113px" width="60" height="60" viewBox="0 0 60 60"><circle cx="30" cy="30" r="26" fill="none" stroke="#fff" stroke-width="5"/><path d="M34 16 L20 30 L34 44" fill="none" stroke="#fff" stroke-width="6"/></svg>
  <svg class="abs hero-arrow" style="left:1028px" width="60" height="60" viewBox="0 0 60 60"><circle cx="30" cy="30" r="26" fill="none" stroke="#fff" stroke-width="5"/><path d="M26 16 L40 30 L26 44" fill="none" stroke="#fff" stroke-width="6"/></svg>
  <div class="hero-list abs">
    <div class="hero-item" style="top:0">
      <h3>Lorem Ipsum dolor</h3><p>Consectetur adipisicing elit, sed</p>
      <svg width="30" height="30" viewBox="0 0 30 30"><circle cx="15" cy="15" r="14" fill="#1b8eaa" stroke="#cfe"/><circle cx="16" cy="8" r="2" fill="#fff"/><path d="M15 11 L13 17 L10 22 M13 17 L17 19 L18 23 M14 13 L19 15" stroke="#fff" stroke-width="2" fill="none"/></svg>
    </div>
    <div class="hero-item" style="top:60px">
      <h3>Ut enim ad minim</h3><p>Nisi ut aliquip ex ea commodo</p>
      <svg width="30" height="30" viewBox="0 0 30 30"><circle cx="15" cy="15" r="14" fill="#1b8eaa" stroke="#cfe"/><path d="M11 10 A7 7 0 1 0 19 10" stroke="#fff" stroke-width="2.5" fill="none"/><line x1="15" y1="7" x2="15" y2="15" stroke="#fff" stroke-width="2.5"/></svg>
    </div>
    <div class="hero-item" style="top:120px">
      <h3>Repreenderit volupate</h3><p>Velit esse cillum dolore eu fugiat</p>
      <svg width="30" height="30" viewBox="0 0 30 30"><circle cx="15" cy="15" r="14" fill="#1b8eaa" stroke="#cfe"/><rect x="9" y="8" width="12" height="14" fill="none" stroke="#fff" stroke-width="2"/><path d="M12 9v12M18 9v12" stroke="#fff"/></svg>
    </div>
    <div class="hero-item" style="top:180px">
      <h3>Occaecat cupidatat</h3><p>Sunt in culpa qui officia deserunt</p>
      <svg width="30" height="30" viewBox="0 0 30 30"><circle cx="15" cy="15" r="14" fill="#1b8eaa" stroke="#cfe"/><text x="15" y="22" text-anchor="middle" font-family="Arial" font-size="19" font-weight="700" fill="#fff">?</text></svg>
    </div>
  </div>
</section>

<section class="promo-band abs">
  <h2>The Best Software in Shaping Lattice Engineering</h2>
  <div class="inquire-btn">inquire service<svg width="7" height="10" viewBox="0 0 7 10"><path d="M1 1 L5 5 L1 9" stroke="#222" stroke-width="2" fill="none"/></svg></div>
</section>

<main class="content abs">
  <h2 class="col-title abs" style="left:136px;top:32px">Services</h2>
  <div class="service abs" style="left:129px;top:89px">
    <div class="icon" role="img" aria-label="Server icon" style="background:linear-gradient(#ddd,#777 50%,#1d2a2e 52%,#2a3b40)"></div>
    <h4>Lorem ipsum dolor sit amet</h4><p>Sed do eiusmod tempor incididunt ut labore et dolore magna aliqua.</p>
  </div>
  <div class="service abs" style="left:129px;top:179px">
    <div class="icon" role="img" aria-label="Monitor with cloud download icon" style="background:linear-gradient(#2a9fd0,#0f3a55);border:3px solid #222"></div>
    <h4>Lorem ipsum dolor sit amet</h4><p>Sed do eiusmod tempor incididunt ut labore et dolore magna aliqua.</p>
  </div>
  <div class="service abs" style="left:129px;top:269px">
    <div class="icon" role="img" aria-label="Cloud with gear icon" style="background:radial-gradient(circle at 40% 40%,#bfe9fa,#3fb3e0 60%,#fff 62%);border-radius:20px"></div>
    <h4>Lorem ipsum dolor sit amet</h4><p>Sed do eiusmod tempor incididunt ut labore et dolore magna aliqua.</p>
  </div>

  <div class="col-rule abs" style="left:420px"></div>

  <h2 class="col-title abs" style="left:455px;top:32px">Why choose us?</h2>
  <div class="why abs" style="left:455px;top:87px"><h4>Secure</h4><p>Lorem ipsum dolor sit amet, consectetur adipisicing elit, sed do eiusmod tempor incididunt ut.</p><a>read more</a></div>
  <div class="why abs" style="left:455px;top:170px"><h4>Robust</h4><p>Lorem ipsum dolor sit amet, consectetur adipisicing elit, sed do eiusmod tempor incididunt ut.</p><a>read more</a></div>
  <div class="why abs" style="left:455px;top:252px"><h4>Interactive</h4><p>Lorem ipsum dolor sit amet, consectetur adipisicing elit, sed do eiusmod tempor incididunt ut.</p><a>read more</a></div>

  <div class="col-rule abs" style="left:767px"></div>

  <h2 class="col-title abs" style="left:797px;top:32px">Who we are</h2>
  <div class="about abs" style="left:797px;top:90px">
    <p>Lorem ipsum dolor sit amet, consectetur adipisicing elit, sed do eiusmod tempor incididunt ut labore et dolore magna aliqua. Ut enim ad minim veniam, quis nostrud exercitation ullamco laboris nisi ut aliquip ex ea commodo consequat.</p>
    <p>Duis aute irure dolor in reprehenderit in voluptate velit esse cillum dolore eu fugiat nulla pariatur. Excepteur sint occaecat cupidatat non proident, sunt in culpa qui officia deserunt mollit anim id est laborum</p>
    <a>read more</a>
  </div>
</main>

<footer>
  <div class="footer-brand abs">Shaping Lattice</div>
  <div class="copyright abs">© Copyright Shaping Lattice 2014</div>
  <div class="footer-col abs" style="left:339px;top:1043px"><h5>Why Us</h5><ul><li>Our Clients</li><li>Technology</li><li>Soft Labs</li></ul></div>
  <div class="footer-col abs" style="left:459px;top:1043px"><h5>Quick Links</h5><ul><li>Lorem ipsum dolor</li><li>Amet consectetuer</li><li>Mauris vel tortor vitae</li><li>Nibh condimentum</li></ul></div>
  <div class="footer-col abs" style="left:659px;top:1043px"><h5>Support</h5><ul><li>Nibh condimentum</li><li>Integer ac lacus</li><li>Sociis natoque</li><li>Enatibus et magnis</li></ul></div>
  <div class="footer-col abs" style="left:859px;top:1043px"><h5>Newsletter:</h5></div>
  <div class="email-field abs">Enter your email here</div>
  <div class="subscribe-btn abs">SUBSCRIBE</div>
</footer>

</body>
</html>
```